Web design for sitter site

We will be launching a sitter site in the coming months that focuses on sitters for children. The name of this site will be KidHaven.com
We will need:
1. main page design
2. site logo designed
3. subpages as well for the look of people's profiles, and job listings, etc (see links below)
We only need the design, photos, font files, etc. We do not need this site coded (no html), a ps job is fine.
Some competing sites in the space include - tendlyhub.com and vurl.com
http://www.brisk-minder.example/images/profile1.jpg
http://quenthollibrary.example/wp-content/uploads/2013/09/vurl-review.png
http://www.palvermont.example/hr/photos/tendly_hub2.jpg
Target Market(s)
Mothers of children, mainly women
Industry/Entity Type
Online
Look and feel

```html
<!DOCTYPE html>
<html lang="en">
<head>
<meta charset="utf-8">
<title>KidHaven – Caregiver Profile</title>
<link href="https://fonts.googleapis.com/css2?family=Arimo:ital,wght@0,400;0,700;1,400&family=Short+Stack&display=swap" rel="stylesheet">
<style>
:root{
  --sky:#0aa3ee;
  --sky-light:#59c3f5;
  --brand-blue:#1488cf;
  --green:#2ec27e;
  --nav-active:#3a9a5c;
  --check:#5a9e2a;
  --rule:#6a9ec4;
  --text:#222;
  --muted:#777;
  --btn-grey:#b4b8c0;
  --box-border:#a9a9a9;
  --thumb-a:#b27a5e;
  --thumb-b:#7fa6bf;
  --white:#fff;
}
*{box-sizing:border-box;margin:0;padding:0}
html,body{width:712px;height:1200px;overflow:hidden;background:var(--white)}
body{position:relative;font-family:"Arimo",Arial,sans-serif;color:var(--text)}
.abs{position:absolute}
.header-wave{position:absolute;left:0;top:0}
.logo{position:absolute;left:27px;top:22px;font-family:"Short Stack",cursive;font-size:36px;color:var(--white);line-height:1;white-space:nowrap}
.logo-tag{position:absolute;left:104px;top:68px;font-family:"Short Stack",cursive;font-size:9px;color:var(--white);white-space:nowrap}
.nav a{position:absolute;top:24px;font-family:"Short Stack",cursive;font-size:9px;line-height:12px;color:var(--white);text-decoration:none;white-space:nowrap}
.nav .active{background:var(--nav-active);top:16px;height:30px;width:62px;line-height:16px;padding-top:8px;text-align:center}
.search{position:absolute;left:584px;top:26px;width:100px;height:20px;background:var(--white);border:1px solid #ccc;font-size:7px;color:#aaa;padding:5px}
.adv-search{position:absolute;right:28px;top:52px;font-size:7px;font-weight:700;color:var(--white);white-space:nowrap}
.profile-name{left:32px;top:162px;font-family:"Short Stack",cursive;font-size:25px;color:var(--brand-blue);white-space:nowrap}
.profile-sub{left:33px;top:194px;font-size:11px;font-weight:700;color:var(--brand-blue)}
.btn-back{position:absolute;width:97px;height:26px;background:var(--btn-grey);color:var(--white);font-size:8px;font-weight:700;text-align:center;line-height:26px}
.rule{position:absolute;height:1px;background:var(--rule)}
.rule.grey{background:#bbb}
.photo{left:35px;top:265px;width:92px;height:123px;background:linear-gradient(160deg,#6b4a3c,#a67b66 55%,#3b2a24)}
.quote{font-style:italic;color:var(--muted);font-size:8.5px;line-height:1.3}
.label{font-size:8px;font-weight:700;color:#444}
.small-grey{font-size:8px;color:var(--muted)}
.price{left:140px;top:349px;font-size:15px;font-weight:700;color:#444}
.meta{left:35px;top:394px;font-size:11px;line-height:1.25}
.btn-hire{left:257px;top:416px;width:67px;height:27px;background:var(--green);color:var(--white);font-size:8px;font-weight:700;text-align:center;line-height:27px}
.section-title{font-size:11px;font-weight:700;color:var(--brand-blue);white-space:nowrap}
.testimonial{position:absolute;left:363px;width:225px}
.testimonial .who{margin-left:152px;margin-top:3px;font-size:8px;font-weight:700;color:#333;line-height:1.3}
.check-item{position:absolute;display:flex;align-items:center;gap:6px;font-size:11px;color:var(--muted);white-space:nowrap}
.check-item svg{width:14px;height:14px}
.history-box{position:absolute;left:37px;width:318px;height:77px;border:1px solid var(--box-border);padding:9px 8px}
.history-box h4{font-size:11px;font-weight:400;color:#222;white-space:nowrap}
.history-box .label{margin-top:18px}
.history-box .small-grey{margin-top:6px}
.side-title{font-size:11px;color:#222}
.person{position:absolute;left:453px;display:flex;gap:13px}
.thumb{width:29px;height:27px}
.thumb.a{background:linear-gradient(135deg,var(--thumb-a),#e3b08f)}
.thumb.b{background:linear-gradient(135deg,var(--thumb-b),#d8e6ef)}
.person .n{font-size:11px;color:#222;line-height:1.15}
.person .d{font-size:8px;color:#555}
.avail-date{font-size:6px;color:var(--brand-blue);font-weight:700;margin-left:4px}
.avail{position:absolute;left:37px;top:914px;border-collapse:collapse}
.avail th{font-size:7px;font-weight:700;color:#444;height:16px;width:37px;text-align:center}
.avail th.row-h{width:70px;text-align:left}
.avail td{height:18px;text-align:center}
.avail td.row-l{text-align:left;font-size:7px;font-weight:700;color:#444;white-space:nowrap}
.avail svg{width:14px;height:14px;display:block;margin:0 auto}
.copyright{left:33px;top:1122px;font-size:8px;font-weight:700;color:var(--brand-blue)}
.social{position:absolute;top:1141px;width:25px;height:26px}
.legal{right:66px;top:1158px;font-size:8px;font-weight:700;color:var(--brand-blue)}
.footer-band{position:absolute;left:0;bottom:0;width:712px;height:19px;background:var(--sky);border-top:3px solid var(--sky-light)}
.footer-band::after{content:"";position:absolute;left:0;top:5px;width:100%;height:2px;background:var(--white)}
</style>
</head>
<body>
<svg width="0" height="0" style="position:absolute">
  <symbol id="tick" viewBox="0 0 14 14">
    <rect x="1" y="3" width="10" height="10" fill="none" stroke="#9bbf7c" stroke-width="1"/>
    <path d="M2.5 7.5 L5.5 11 L13 1.5" fill="none" stroke="#5a9e2a" stroke-width="2.4" stroke-linecap="round" stroke-linejoin="round"/>
  </symbol>
  <symbol id="box" viewBox="0 0 14 14">
    <rect x="2" y="3" width="10" height="10" fill="#fff" stroke="#9bbf7c" stroke-width="1"/>
  </symbol>
</svg>

<header>
  <svg class="header-wave" width="712" height="140" viewBox="0 0 712 140">
    <path d="M0 0H712V112C620 128 540 98 420 110C300 122 180 96 0 126Z" fill="#59c3f5"/>
    <path d="M0 0H712V104C620 120 540 92 420 102C300 114 180 88 0 118Z" fill="#0aa3ee"/>
  </svg>
  <div class="logo">KidHaven</div>
  <div class="logo-tag">best care ever</div>
  <nav class="nav">
    <a style="left:267px">Home Care</a>
    <a class="active" style="left:333px">Child Care</a>
    <a style="left:408px">Pet Care</a>
    <a style="left:475px">Senior Care</a>
  </nav>
  <div class="search">search</div>
  <div class="adv-search">Advance Search</div>
</header>

<main>
  <h1 class="abs profile-name">Sharon M. Shields</h1>
  <div class="abs profile-sub">28yrs., Female, Arizona, USA</div>
  <div class="btn-back" style="left:555px;top:184px">Back to listings</div>
  <div class="rule" style="left:27px;top:233px;width:626px"></div>

  <div class="abs photo" role="img" aria-label="Portrait photo of the caregiver"></div>
  <p class="abs quote" style="left:140px;top:268px;width:160px">" I love kids! Hire me and you'll have no worries ;)"</p>
  <div class="abs label" style="left:140px;top:314px">Skills:</div>
  <div class="abs small-grey" style="left:140px;top:328px">Basic Cooking, Cleaning, Etc.</div>
  <div class="abs price">$18 / hr</div>
  <div class="abs meta">Part-time<br>5yrs of exp.</div>
  <div class="abs btn-hire">HIRE ME</div>

  <h2 class="abs section-title" style="left:366px;top:257px">Sharon's Testimonials:</h2>
  <div class="testimonial" style="top:288px">
    <p class="quote">" My kids are so happy when she's around. I got nothing to worry about when she's here..."</p>
    <div class="who">Steven Polen,<br>New York, USA</div>
  </div>
  <div class="testimonial" style="top:351px">
    <p class="quote">" My kids are so happy when she's around. I got nothing to worry about when she's here..."</p>
    <div class="who">Steven Polen,<br>New York, USA</div>
  </div>
  <div class="testimonial" style="top:416px">
    <p class="quote">" My kids are so happy when she's around. I got nothing to worry about when she's here..."</p>
    <div class="who">Steven Polen,<br>New York, USA</div>
  </div>

  <div class="rule grey" style="left:27px;top:476px;width:658px"></div>

  <h2 class="abs section-title" style="left:37px;top:500px">Do's &amp; Dont's</h2>
  <div class="check-item" style="left:40px;top:525px"><svg><use href="#tick"/></svg>Don't Smoke</div>
  <div class="check-item" style="left:40px;top:551px"><svg><use href="#tick"/></svg>Comfortable with pets</div>
  <div class="check-item" style="left:40px;top:576px"><svg><use href="#tick"/></svg>Single Mom</div>
  <div class="check-item" style="left:40px;top:601px"><svg><use href="#tick"/></svg>Willing to travel 50mi</div>
  <div class="check-item" style="left:177px;top:525px"><svg><use href="#tick"/></svg>Has own transport</div>
  <div class="check-item" style="left:177px;top:551px"><svg><use href="#tick"/></svg>CPR Certified</div>
  <div class="check-item" style="left:177px;top:576px"><svg><use href="#tick"/></svg>With 2 kids</div>

  <h2 class="abs section-title" style="left:376px;top:495px">Payment Preferences:</h2>
  <div class="check-item" style="left:381px;top:526px"><svg><use href="#tick"/></svg>PayNimbus</div>
  <div class="check-item" style="left:381px;top:543px"><svg><use href="#tick"/></svg>Credit Card</div>
  <div class="check-item" style="left:381px;top:561px"><svg><use href="#tick"/></svg>Cash</div>
  <div class="check-item" style="left:381px;top:580px"><svg><use href="#tick"/></svg>Personal Checks</div>
  <div class="check-item" style="left:381px;top:599px"><svg><use href="#tick"/></svg>Wire Transfers</div>

  <div class="rule grey" style="left:37px;top:643px;width:648px"></div>

  <h2 class="abs section-title" style="left:37px;top:662px">Work History:</h2>
  <div class="history-box" style="top:683px">
    <h4>Babysitter - Taresa M. family &nbsp; (Jun. 2012 - Apr. 2014)</h4>
    <div class="label">Responsibilities:</div>
    <div class="small-grey">Cooking/Meal Preparation, Swiming supervision</div>
  </div>
  <div class="history-box" style="top:772px">
    <h4>Caregiver - Augusto P. family &nbsp; (May. 2013 - Dec. 2014)</h4>
    <div class="label">Responsibilities:</div>
    <div class="small-grey">Adult / Senior Supervision, CPR certified</div>
  </div>
  <div class="rule grey" style="left:37px;top:869px;width:318px"></div>

  <h3 class="abs side-title" style="left:440px;top:697px">Related Caregivers:</h3>
  <div class="person" style="top:719px"><div class="thumb a" role="img" aria-label="Caregiver photo"></div><div><div class="n">Meyll B. Pauls</div><div class="d">28yrs. , Arizona, USA</div></div></div>
  <div class="person" style="top:752px"><div class="thumb b" role="img" aria-label="Caregiver photo"></div><div><div class="n">Danielle</div><div class="d">20yrs. , New York, USA</div></div></div>
  <div class="person" style="top:785px"><div class="thumb a" role="img" aria-label="Caregiver photo"></div><div><div class="n">Meyll B. Pauls</div><div class="d">28yrs. , Arizona, USA</div></div></div>
  <div class="person" style="top:818px"><div class="thumb b" role="img" aria-label="Caregiver photo"></div><div><div class="n">Danielle</div><div class="d">20yrs. , New York, USA</div></div></div>

  <h3 class="abs side-title" style="left:440px;top:871px">Recently Viewed:</h3>
  <div class="person" style="top:894px"><div class="thumb a" role="img" aria-label="Caregiver photo"></div><div><div class="n">Meyll B. Pauls</div><div class="d">28yrs. , Arizona, USA</div></div></div>
  <div class="person" style="top:927px"><div class="thumb b" role="img" aria-label="Caregiver photo"></div><div><div class="n">Danielle</div><div class="d">20yrs. , New York, USA</div></div></div>
  <div class="person" style="top:960px"><div class="thumb a" role="img" aria-label="Caregiver photo"></div><div><div class="n">Meyll B. Pauls</div><div class="d">28yrs. , Arizona, USA</div></div></div>
  <div class="person" style="top:993px"><div class="thumb b" role="img" aria-label="Caregiver photo"></div><div><div class="n">Danielle</div><div class="d">20yrs. , New York, USA</div></div></div>

  <h2 class="abs section-title" style="left:37px;top:891px">Availability: <span class="avail-date">As of 08/01/14 to 11/30/14</span></h2>
  <table class="avail">
    <tr><th class="row-h"></th><th>Sun</th><th>Mon</th><th>Tues</th><th>Wed</th><th>Thurs</th><th>Fri</th><th>Sat</th></tr>
    <tr><td class="row-l">Early Morning</td><td><svg><use href="#tick"/></svg></td><td><svg><use href="#tick"/></svg></td><td><svg><use href="#tick"/></svg></td><td><svg><use href="#tick"/></svg></td><td><svg><use href="#tick"/></svg></td><td><svg><use href="#box"/></svg></td><td><svg><use href="#tick"/></svg></td></tr>
    <tr><td class="row-l">Late Morning</td><td><svg><use href="#tick"/></svg></td><td><svg><use href="#tick"/></svg></td><td><svg><use href="#tick"/></svg></td><td><svg><use href="#tick"/></svg></td><td><svg><use href="#tick"/></svg></td><td><svg><use href="#box"/></svg></td><td><svg><use href="#tick"/></svg></td></tr>
    <tr><td class="row-l">Early Afternoon</td><td><svg><use href="#tick"/></svg></td><td><svg><use href="#box"/></svg></td><td><svg><use href="#tick"/></svg></td><td><svg><use href="#tick"/></svg></td><td><svg><use href="#tick"/></svg></td><td><svg><use href="#box"/></svg></td><td><svg><use href="#tick"/></svg></td></tr>
    <tr><td class="row-l">Late Afternoon</td><td><svg><use href="#tick"/></svg></td><td><svg><use href="#tick"/></svg></td><td><svg><use href="#tick"/></svg></td><td><svg><use href="#tick"/></svg></td><td><svg><use href="#tick"/></svg></td><td><svg><use href="#tick"/></svg></td><td><svg><use href="#tick"/></svg></td></tr>
    <tr><td class="row-l">Early Evening</td><td><svg><use href="#tick"/></svg></td><td><svg><use href="#tick"/></svg></td><td><svg><use href="#tick"/></svg></td><td><svg><use href="#tick"/></svg></td><td><svg><use href="#tick"/></svg></td><td><svg><use href="#box"/></svg></td><td><svg><use href="#tick"/></svg></td></tr>
    <tr><td class="row-l">Late Evening</td><td><svg><use href="#box"/></svg></td><td><svg><use href="#tick"/></svg></td><td><svg><use href="#tick"/></svg></td><td><svg><use href="#tick"/></svg></td><td><svg><use href="#tick"/></svg></td><td><svg><use href="#tick"/></svg></td><td><svg><use href="#tick"/></svg></td></tr>
    <tr><td class="row-l">Overnight</td><td><svg><use href="#tick"/></svg></td><td><svg><use href="#tick"/></svg></td><td><svg><use href="#tick"/></svg></td><td><svg><use href="#tick"/></svg></td><td><svg><use href="#tick"/></svg></td><td><svg><use href="#box"/></svg></td><td><svg><use href="#tick"/></svg></td></tr>
  </table>

  <div class="rule" style="left:37px;top:1072px;width:616px"></div>
  <div class="btn-back" style="left:555px;top:1083px">Back to listings</div>
</main>

<footer>
  <div class="abs copyright">(c) copyright 2014 KidHaven.com</div>
  <div class="social" style="left:32px;background:#3b5a96" role="img" aria-label="Social link"></div>
  <div class="social" style="left:60px;background:#33a7de" role="img" aria-label="Social link"></div>
  <div class="social" style="left:88px;background:#d4483a" role="img" aria-label="Social link"></div>
  <div class="social" style="left:116px;background:#c2302a" role="img" aria-label="Social link"></div>
  <div class="abs legal">Terms | Policy | Careers</div>
  <div class="footer-band"></div>
</footer>
</body>
</html>
```